Brisk Hounds Dog Behaviour, Training and Natural Healthcare Business Card Design

I am an experienced and qualified dog behavioural trainer and natural animal healthcare consultant offering a range of services to help pet dog owners with the "whole dog".
COLOURS: A soft light blue in the background - can be fading out or split, red should also feature
LOGO: Dog, healing hands, silhouette, shadow
SERVICES: Behaviour Consults, Training, Complex Skills Coaching Walking Coaching, Diet & Nutrition, Environmental Enrichment, Lifestyle and Lifestage Adaptations, Massage, Natural Health Options
BY LINE: Happy Dogs, Happy Owners
VALUES: Promoting communication and connection between dogs and their owners.
FOCUS: Nutritional guidance and environmental adaptation are often needed to complete the package and increase the success rate of training and behaviour modification.

Target Market(s)

Everyone who has a dog who they wish to improve their relationship with

Industry/Entity Type

Communication

Contact Information for Business Card

Brisk Hounds, Renata Walcott, 0472 680351, briskhounds7@mailnest.example, www.briskhounds7.example, Qualified Dog Behavioural Trainer and Natural Animal Healthcare Consultant

Font styles to use
Sans Serif
Script

Colors
85cae6
ec2027

Requirements
Must have
• A clear indication that it is a dog services business. A raised feature
Should not have
• Pawprints, cartoons

```html
<!DOCTYPE html>
<html lang="en">
<head>
<meta charset="utf-8">
<title>Brisk Hounds – Business Card</title>
<link rel="stylesheet" href="https://fonts.googleapis.com/css2?family=Arimo:wght@400;700&family=PT+Sans:wght@400&family=Tinos:wght@400&display=swap">
<style>
  :root {
    --page-bg: #ececec;
    --card-white: #ffffff;
    --brand-red: #ec2027;
    --brand-red-deep: #b8232b;
    --sky-light: #85cae6;
    --sky-mid: #3aaee0;
    --sky-deep: #1996cf;
    --rule-blue: #1a8fd6;
    --ink: #1a1a1a;
    --on-blue: #ffffff;
  }
  * { box-sizing: border-box; margin: 0; padding: 0; }
  html, body {
    width: 1200px; height: 900px; overflow: hidden;
    background: var(--page-bg);
  }
  .business-card {
    position: absolute; left: 150px; top: 180px;
    width: 900px; height: 540px;
    background: var(--card-white);
    overflow: hidden;
    box-shadow: 0 10px 30px rgba(0,0,0,0.25);
  }
  .band-top {
    position: absolute; left: 0; top: 0; width: 100%; height: 28px;
    background: linear-gradient(90deg, var(--brand-red-deep), var(--brand-red) 50%, var(--brand-red-deep));
  }
  .band-bottom {
    position: absolute; left: 0; bottom: 0; width: 100%; height: 80px;
    background: linear-gradient(90deg, var(--brand-red-deep), var(--brand-red) 45%, var(--brand-red-deep));
  }
  .contact-panel {
    position: absolute; left: 0; top: 228px; width: 100%; height: 232px;
    background: linear-gradient(90deg, var(--sky-deep) 0%, var(--sky-mid) 35%, var(--sky-light) 62%, var(--sky-mid) 100%);
  }
  .panel-pointer {
    position: absolute; left: 812px; top: 228px;
    width: 40px; height: 24px;
  }
  .dog-outline-art {
    position: absolute; left: 10px; top: 250px;
    width: 380px; height: 210px;
    background: radial-gradient(ellipse at 55% 45%, rgba(255,255,255,0.22), rgba(255,255,255,0) 70%);
  }
  .dog-photo-wash {
    position: absolute; left: 360px; top: 228px;
    width: 540px; height: 232px;
    background: radial-gradient(ellipse at 60% 40%, rgba(255,255,255,0.28), rgba(255,255,255,0) 65%);
  }
  .brand {
    position: absolute; left: 40px; top: 50px; width: 260px;
    text-align: center;
  }
  .brand-mark {
    display: block; width: 110px; height: 110px; margin: 0 auto 8px;
    border-radius: 50%; background: var(--brand-red-deep);
  }
  .brand-name {
    font-family: "Arimo", Arial, sans-serif; font-weight: 700;
    font-size: 40px; line-height: 1; color: var(--brand-red);
    white-space: nowrap;
  }
  .holder {
    position: absolute; left: 470px; top: 60px; width: 400px;
    text-align: center;
  }
  .holder-name {
    font-family: "Arimo", Arial, sans-serif; font-weight: 700;
    font-size: 40px; color: var(--brand-red); line-height: 1.1;
  }
  .holder-rule {
    width: 270px; height: 2px; margin: 6px auto 12px;
    background: var(--rule-blue);
  }
  .holder-title {
    font-family: "Tinos", "Times New Roman", serif;
    font-size: 21px; line-height: 1.2; color: var(--ink);
  }
  .contact-list {
    position: absolute; left: 490px; top: 285px;
    list-style: none;
  }
  .contact-item {
    display: flex; align-items: center; gap: 10px;
    height: 52px;
    font-family: "PT Sans", Arial, sans-serif;
    font-size: 25px; color: var(--on-blue);
  }
  .contact-icon { width: 28px; height: 28px; flex: none; }
</style>
</head>
<body>
  <main class="business-card">
    <div class="band-top"></div>

    <div class="brand">
      <span class="brand-mark"></span>
      <div class="brand-name">Brisk Hounds</div>
    </div>

    <div class="holder">
      <h1 class="holder-name">Renata Walcott</h1>
      <div class="holder-rule"></div>
      <p class="holder-title">Dog Behavioural Trainer and<br>Natural Animal Healthcare Consultant</p>
    </div>

    <section class="contact-panel"></section>
    <div class="dog-photo-wash" role="img" aria-label="Soft close-up photograph of a dog's face faded into the blue background"></div>
    <div class="dog-outline-art" role="img" aria-label="White line drawing of a standing dog in profile"></div>
    <svg class="panel-pointer" viewBox="0 0 40 24" aria-hidden="true">
      <polygon points="0,0 40,0 20,24" fill="#ffffff"/>
    </svg>

    <ul class="contact-list">
      <li class="contact-item">
        <svg class="contact-icon" viewBox="0 0 28 28" aria-hidden="true">
          <rect width="28" height="28" rx="5" fill="#ffffff"/>
          <path d="M8 7c1.5-1 2.5-.5 3.2 1l1 2c.4.9 0 1.5-.7 2l-.6.4c.8 1.8 2 3 3.8 3.8l.4-.6c.5-.7 1.1-1.1 2-.7l2 1c1.5.7 2 1.7 1 3.2-1 1.4-2.5 1.8-4.3 1.2C11.5 19.8 8.2 16.5 6.8 12 6.2 10 6.6 8 8 7z" fill="#1996cf"/>
        </svg>
        <span>0472 680351</span>
      </li>
      <li class="contact-item">
        <svg class="contact-icon" viewBox="0 0 28 28" aria-hidden="true">
          <rect width="28" height="28" rx="5" fill="#ffffff"/>
          <rect x="5" y="8" width="18" height="13" rx="1.5" fill="none" stroke="#1996cf" stroke-width="2"/>
          <polyline points="5,9 14,16 23,9" fill="none" stroke="#1996cf" stroke-width="2"/>
        </svg>
        <span>briskhounds7@mailnest.example</span>
      </li>
      <li class="contact-item">
        <svg class="contact-icon" viewBox="0 0 28 28" aria-hidden="true">
          <rect width="28" height="28" rx="5" fill="#ffffff"/>
          <circle cx="14" cy="14" r="8" fill="none" stroke="#1996cf" stroke-width="2"/>
          <ellipse cx="14" cy="14" rx="3.5" ry="8" fill="none" stroke="#1996cf" stroke-width="1.6"/>
          <line x1="6" y1="14" x2="22" y2="14" stroke="#1996cf" stroke-width="1.6"/>
        </svg>
        <span>www.briskhounds7.example</span>
      </li>
    </ul>

    <div class="band-bottom"></div>
  </main>
</body>
</html>
```